Business card design for new brand

We have recently rebranded and need a new business card template.

We are an insurance underwriting agency. All of our products are sold via other partner companies, so these are just to pass on our details to other organisations.

We would like to see designs that use the colour green (current stationary generally uses lime green (rgb 142,190,63) and forest green (0,154,79) to comply with our logo's colours. We are happy with other shades of green.

Business cards need to include our logo, as well as space for:
1. Full name
2. Qualifications (optional)
3. Title
4. Office number
5. Mobile number
6. Email address

Our logo is enclosed here.

```html
<!DOCTYPE html>
<html lang="en">
<head>
<meta charset="UTF-8">
<title>Greenvale Underwriting – Business Card</title>
<link rel="stylesheet" href="https://fonts.googleapis.com/css2?family=Exo+2:wght@400;500&display=swap">
<style>
  :root {
    --backdrop: #dcdcdc;
    --card: #ffffff;
    --lime: #8ebe3f;
    --lime-deep: #78b22f;
    --forest: #009a4f;
    --forest-deep: #008a45;
    --ink: #111111;
  }
  html, body {
    margin: 0;
    width: 1200px;
    height: 900px;
    overflow: hidden;
    background: var(--backdrop);
  }
  .business-card {
    position: absolute;
    left: 75px;
    top: 150px;
    width: 1050px;
    height: 600px;
    background: var(--card);
    font-family: "Exo 2", sans-serif;
    color: var(--ink);
    overflow: hidden;
  }
  .card-shapes {
    position: absolute;
    inset: 0;
  }
  .brand {
    position: absolute;
    left: 560px;
    top: 95px;
    display: flex;
    align-items: center;
    gap: 16px;
  }
  .brand-square {
    width: 46px;
    height: 46px;
    background: var(--forest);
  }
  .brand-name {
    font-size: 44px;
    font-weight: 500;
    line-height: 1;
    color: var(--ink);
  }
  .brand-tagline {
    font-size: 22px;
    font-weight: 500;
    margin-top: 6px;
    color: var(--ink);
  }
  .holder {
    position: absolute;
    left: 150px;
    top: 318px;
  }
  .holder-name {
    font-size: 38px;
    font-weight: 500;
    margin: 0;
    line-height: 1.1;
  }
  .holder-title {
    display: flex;
    align-items: center;
    gap: 8px;
    margin-top: 4px;
    font-size: 26px;
    color: var(--forest);
  }
  .holder-title::before {
    content: "";
    width: 58px;
    height: 2px;
    background: var(--forest);
    margin-top: 8px;
  }
  .contact-list {
    list-style: none;
    margin: 34px 0 0 12px;
    padding: 0;
    font-size: 20px;
    line-height: 1.45;
  }
  .contact-item {
    display: flex;
    align-items: flex-start;
    gap: 10px;
  }
  .contact-item + .contact-item { margin-top: 8px; }
  .contact-icon {
    width: 18px;
    height: 18px;
    margin-top: 8px;
    flex: none;
  }
</style>
</head>
<body>
  <section class="business-card">
    <svg class="card-shapes" viewBox="0 0 1050 600" width="1050" height="600" aria-hidden="true">
      <defs>
        <linearGradient id="lime-band" x1="0" y1="0" x2="1" y2="1">
          <stop offset="0" stop-color="var(--lime)"/>
          <stop offset="1" stop-color="var(--lime-deep)"/>
        </linearGradient>
        <linearGradient id="forest-band" x1="0" y1="0" x2="0" y2="1">
          <stop offset="0" stop-color="var(--forest)"/>
          <stop offset="1" stop-color="var(--forest-deep)"/>
        </linearGradient>
      </defs>
      <polygon points="0,0 500,0 200,200 0,95" fill="url(#lime-band)"/>
      <polygon points="1050,260 900,390 900,600 1050,600" fill="url(#forest-band)"/>
    </svg>

    <div class="brand">
      <div class="brand-square"></div>
      <div>
        <div class="brand-name">Greenvale</div>
        <div class="brand-tagline">Underwriting Pty Ltd</div>
      </div>
    </div>

    <div class="holder">
      <h1 class="holder-name">Your Name Goes Here</h1>
      <div class="holder-title">Title</div>
      <ul class="contact-list">
        <li class="contact-item">
          <svg class="contact-icon" viewBox="0 0 18 18" aria-hidden="true">
            <circle cx="9" cy="9" r="8" fill="none" stroke="var(--forest)" stroke-width="2"/>
            <path d="M6 5.5 L7.5 5 L8.3 7 L7.4 7.8 Q8.2 9.8 10.2 10.6 L11 9.7 L13 10.5 L12.5 12 Q8 12.5 5.5 7.5 Z" fill="var(--forest)"/>
          </svg>
          <span>+123468798<br>+123468798</span>
        </li>
        <li class="contact-item">
          <svg class="contact-icon" viewBox="0 0 18 18" aria-hidden="true">
            <rect x="1" y="3.5" width="16" height="11" fill="none" stroke="var(--forest)" stroke-width="1.8"/>
            <path d="M1 3.5 L9 10 L17 3.5 M1 14.5 L7 8.5 M17 14.5 L11 8.5" fill="none" stroke="var(--forest)" stroke-width="1.5"/>
          </svg>
          <span>email@mail.com</span>
        </li>
      </ul>
    </div>
  </section>
</body>
</html>
```